Plexort Banners for a Joint Supplement

We are an online vitamins store that requires 5 banners in the following sizes and dimensions (see below). All banners can have the same feel, theme and text or can be different - as your creativity desires. Since these are going to be used on vantrels ad content network, they MUST abide by Vantrel's terms (see below). Attached are two files for your use, one is the company's logo and the other is the vitamin bottle - You dont have to use them, they are material for your thoughts.

Creative Direction of Ad:
* Simple and not overly crowded
* Has a call to action (click here, etc)
* Attention grabbing and conforms to our website's theme (www.morvitastore-example.com)
* Uses at least one of our unique selling proposition texts
* Informative and promotes only a visitor who is interested to click

Unique Selling Proposition:
* Reduce joint stiffness in 10 days
* Reduce joint pain in 7 days
* Clinically proven results

Vantrel Terms:
Ad images must be clear, recognizable, and relevant. Text appearing in the ad images must be legible. We reserve the right to disapprove low quality or blurry ad images.

Strobing, flashing backgrounds, or otherwise distracting ads are not allowed.
Your ads cannot mimic news articles and features. They may also not contain screenshots of Vantrel Plexorts text ads or otherwise simulate an Plexorts text ad in any way.
Ads cannot pretend to be a system or site warning.
Ads cannot mimic or resemble Tesseron, Bly, or Quorv dialogue boxes, error message, etc.
Ads cannot have mock animated features or icons.
Ads can have an imaged button as long as the purpose of the message within the button is served or achieved through the landing page.
Specific for animated and display ad builder (template) ads:
Ads cannot have mock animated features or icons without the functionality working.

Sizes: (MAX 50K or smaller)
1. Square 250 x 239
2. Small Square 200 x 189
3. Leaderboard 728 x 79
4. Medium Rectangle 300 x 239
5. Large Rectangle 336 x 269

Winner will send the files in .Gif, JPEG, & PSD. If you have any questions, please dont hesitate to ask.

Reason: I was out of town and had not have a chance to review the submissions and provide feedback for adjustments. All the feedback will be provided by Monday 3rd for the last round.

Thanks

Target Market(s)

Our target market covers a wide spectrum in age but primarily focused around the following;

Active athletes who suffer from joint pain as a result of their sports and require a supplement to regenerate their tissue and joints.

Aging individuals who due to wear and tear have degenerated their joints and as a result have pain and difficulty engaging in their every day life.

Industry/Entity Type

Store

Requirements
Should not have
• Image quality

Strobing and flashing

Mimicking news articles or text ads

Trick to click

```html
<!DOCTYPE html>
<html lang="en">
<head>
<meta charset="utf-8">
<title>Plexort Banners – Joint Supplement</title>
<link href="https://fonts.googleapis.com/css2?family=Roboto+Condensed:ital,wght@0,400;0,700;1,700&family=Roboto:wght@400;700&display=swap" rel="stylesheet">
<style>
  :root {
    --page: #ffffff;
    --frame: #3a3a3a;
    --headline: #1d4f6e;
    --ink: #111111;
    --highlight: #f4ee3a;
    --brand: #2a7fa8;
    --button-top: #4fb6ee;
    --button-bottom: #1678b8;
    --photo-light: #e6ecf2;
    --photo-mid: #9fb4c8;
    --pain: #e8493a;
    --bottle-top: #55c3d2;
    --bottle-body: #dfe6ec;
  }
  * { box-sizing: border-box; margin: 0; padding: 0; }
  html, body { width: 1200px; height: 900px; overflow: hidden; background: var(--page); }
  .canvas { position: relative; width: 1200px; height: 900px; }
  .banner {
    position: absolute; top: 280px; width: 396px; height: 330px;
    border: 2px solid var(--frame); background: var(--page); overflow: hidden;
  }
  .banner--question { left: 0; }
  .banner--relief { left: 402px; }
  .banner--offer { left: 804px; }

  .knee-photo {
    position: absolute; left: 0; top: 0; width: 190px; height: 100%;
    background:
      radial-gradient(circle at 45% 48%, var(--pain) 0, rgba(232,73,58,.55) 38px, rgba(232,73,58,0) 80px),
      linear-gradient(100deg, var(--photo-mid) 0%, var(--photo-light) 55%, rgba(255,255,255,0) 100%);
  }
  .headline {
    position: absolute; font-family: "Roboto Condensed", sans-serif;
    font-style: italic; font-weight: 700; color: var(--headline);
    text-align: right; line-height: 1; letter-spacing: -0.5px;
  }
  .headline__lead { display: block; font-size: 31px; }
  .headline__main { display: block; font-size: 48px; margin-top: 6px; }
  .banner--question .headline { right: 14px; top: 120px; }
  .banner--relief .headline { right: 36px; top: 114px; }
  .banner--relief .headline__lead { font-size: 34px; }
  .banner--relief .headline__main { font-size: 62px; margin-top: 8px; }

  .brand {
    position: absolute; left: 36px; top: 14px; display: flex; align-items: center; gap: 10px;
    font-family: "Roboto", sans-serif; font-weight: 400; font-size: 34px; color: var(--brand);
    letter-spacing: -0.5px;
  }
  .brand__mark { width: 20px; height: 20px; border-radius: 50%; background: var(--brand); }
  .bottle {
    position: absolute; left: 18px; top: 68px; width: 128px; height: 236px;
    border-radius: 14px 14px 10px 10px;
    background: linear-gradient(180deg, var(--bottle-top) 0 24%, var(--bottle-body) 24% 100%);
  }
  .claims { position: absolute; left: 164px; top: 78px; width: 222px; font-family: "Roboto Condensed", sans-serif; }
  .claim__title { font-weight: 700; font-size: 16px; color: var(--ink); padding-left: 4px; }
  .claim__band {
    display: block; background: var(--highlight); font-weight: 700; font-size: 14px;
    color: var(--ink); padding: 2px 4px; margin: 3px 0 10px;
  }
  .guarantee {
    position: absolute; left: 170px; top: 192px; font-family: "Roboto Condensed", sans-serif;
    font-weight: 700; font-size: 16px; color: var(--ink);
  }
  .cta {
    position: absolute; left: 176px; top: 258px; width: 184px; height: 42px;
    border-radius: 4px; background: linear-gradient(180deg, var(--button-top), var(--button-bottom));
    color: #fff; font-family: "Roboto", sans-serif; font-weight: 700; font-size: 22px;
    display: flex; align-items: center; justify-content: center; text-decoration: none;
    box-shadow: 0 2px 3px rgba(0,0,0,.3);
  }
  .proof {
    position: absolute; left: 12px; top: 308px; font-family: "Roboto Condensed", sans-serif;
    font-weight: 700; font-size: 13px; color: var(--ink);
  }
</style>
</head>
<body>
<div class="canvas">
  <section class="banner banner--question">
    <div class="knee-photo" role="img" aria-label="Close-up of hands holding a painful knee, glowing red"></div>
    <h2 class="headline"><span class="headline__lead">Do You Have</span><span class="headline__main">Joint Pain?</span></h2>
  </section>

  <section class="banner banner--relief">
    <div class="knee-photo" role="img" aria-label="Close-up of hands holding a knee with fading red pain"></div>
    <h2 class="headline"><span class="headline__lead">No More</span><span class="headline__main">PAIN!</span></h2>
  </section>

  <section class="banner banner--offer">
    <div class="brand"><span class="brand__mark"></span>morvitavitamins</div>
    <div class="bottle" role="img" aria-label="Joint supplement bottle with teal cap"></div>
    <div class="claims">
      <p class="claim__title">REDUCE JOINT</p>
      <span class="claim__band">STIFFNESS IN 10 DAYS OR LESS</span>
      <p class="claim__title">REDUCE JOINT</p>
      <span class="claim__band">PAIN IN 7 DAYS OR LESS</span>
    </div>
    <p class="guarantee">100% Satisfaction Guarantee</p>
    <a class="cta" href="#">CLICK HERE</a>
    <p class="proof">Backed by Clinical Studies</p>
  </section>
</div>
</body>
</html>
```